Podcast Cover Art for Fast Growing Show (Ill include a gracious tip!)

This artwork is for "The Steadfast Fellow Show." The podcast is for men, and it's all about self-improvement, confidence, success, money, women and masculinity. It's for the guy who wants to improve himself. I'd like for my picture to be included — in black and white — and I want the text to read: "The Steadfast Fellow Show" and somewhere in there it'll say: "with Dale Prowen." I'm open to color schemes. The podcast is a little edgy so I'd like for that to be represented in the design. Thank you! (((Here's the podcast page if you wanna check it out: http://steadfastfellowshow.castorbit.net/)))

Target Market(s)

Men who want to attract women and improve their lives!

Font styles to use
Serif

Colors

Designer to choose colors to be used in the design.

Requirements
Must have
• My image in it (in black and white) and the two titles: "The Steadfast Fellow Show" and "with Dale Prowen"
Nice to have
• My logo in it somehow (which is the arrow looking logo attached below). I've also found that my image looks best in black and white and with a circular type cut out (although I'm open to different design ideas). I've attached my logo with a circular cut out below so you can see what I'm talking about.
Should not have
• Flowers. Teddy bears. ice cream.

```html
<!DOCTYPE html>
<html lang="en">
<head>
<meta charset="utf-8">
<title>The Steadfast Fellow Show — Cover Art</title>
<link href="https://fonts.googleapis.com/css2?family=Roboto+Condensed:wght@700&family=Roboto:wght@700&display=swap" rel="stylesheet">
<style>
  :root {
    --ink: #000000;
    --paper: #ffffff;
    --accent: #f7a10a;
    --grey-light: #8a8a8a;
    --grey-mid: #4a4a4a;
    --grey-dark: #1a1a1a;
  }
  html, body {
    margin: 0;
    padding: 0;
    width: 1200px;
    height: 1200px;
    overflow: hidden;
    background: var(--ink);
  }
  .cover {
    position: relative;
    width: 1200px;
    height: 1200px;
    background: var(--ink);
    overflow: hidden;
    font-family: "Roboto Condensed", "Roboto", sans-serif;
  }
  .host-portrait {
    position: absolute;
    right: 0;
    top: 100px;
    width: 740px;
    height: 1100px;
    background:
      radial-gradient(ellipse 38% 30% at 68% 34%, var(--grey-light) 0%, var(--grey-mid) 55%, transparent 100%),
      radial-gradient(ellipse 55% 45% at 62% 85%, var(--grey-dark) 0%, #0d0d0d 70%, transparent 100%),
      linear-gradient(90deg, var(--ink) 0%, rgba(0,0,0,0) 35%);
  }
  .show-title {
    position: absolute;
    left: 74px;
    top: 212px;
    margin: 0;
    font-weight: 700;
    font-size: 118px;
    line-height: 118px;
    letter-spacing: 2px;
    text-transform: uppercase;
    color: var(--paper);
  }
  .show-title .accent { color: var(--accent); }
  .show-title span { display: block; }
  .title-rule {
    position: absolute;
    left: 0;
    top: 619px;
    width: 794px;
    height: 13px;
    background: var(--accent);
  }
  .byline {
    position: absolute;
    left: 74px;
    top: 728px;
    height: 94px;
    display: flex;
    align-items: center;
    gap: 24px;
    font-family: "Roboto", sans-serif;
    font-weight: 700;
    color: var(--paper);
    font-size: 58px;
  }
  .byline .host-name {
    background: var(--accent);
    color: var(--ink);
    height: 94px;
    padding: 0 22px;
    display: flex;
    align-items: center;
    font-family: "Roboto Condensed", sans-serif;
    font-size: 64px;
    letter-spacing: 1px;
    text-transform: uppercase;
  }
  .brand-mark {
    position: absolute;
    left: 74px;
    top: 940px;
    display: flex;
    align-items: center;
    gap: 16px;
    font-weight: 700;
    font-size: 40px;
    letter-spacing: 1px;
    color: var(--paper);
    text-transform: uppercase;
  }
  .brand-mark .dot {
    width: 22px;
    height: 22px;
    background: var(--paper);
  }
</style>
</head>
<body>
  <main class="cover">
    <div class="host-portrait" role="img" aria-label="Black and white portrait of host Dale Prowen, hands steepled in front of his chin"></div>

    <h1 class="show-title">
      <span>The</span>
      <span class="accent">Steadfast</span>
      <span><span class="accent" style="display:inline">Fellow</span> Show</span>
    </h1>

    <div class="title-rule"></div>

    <p class="byline">
      <span class="with">with</span>
      <span class="host-name">Dale Prowen</span>
    </p>

    <div class="brand-mark">
      <span class="dot"></span>
      <span class="brand-name">Steadfast</span>
    </div>
  </main>
</body>
</html>
```